Book Cover: A Quiet Cartographer

DO NOT JUST COPY THE BOOK COVER I HAVE ADDED FOR REFERENCE. I NEED SOMETHING FRESH NOT JUST A COPY AND PASTE!
If you cannot improve on the design with something creative then don't submit a design.

Project Title:
Book Cover Design for A Quiet Cartographer

Must be better than the mock design I have uploaded in project files.

Project Description:
I’m looking for a striking and emotionally evocative book cover for my upcoming title A Quiet Cartographer. This is a deeply personal and powerful memoir about the masks we wear, emotional survival, control, and the journey toward radical self-awareness and healing. The cover should visually represent the contrast between the performative self and the authentic self.

Visual Concept:
Please take visual inspiration and design continuity from my previous book Run FAR Now! — I will upload that cover for reference. This new design should feel like a continuation of the same author journey, but bolder and more psychologically intense.

You’ll be provided with two photos of me:

One where I appear more unkept, raw, and emotionally heavy.

One where I appear clean, centered, and lighter.

These can either be:

Split down the middle to create a “mirror” or duality effect (symbolizing the split self),

Or placed side by side as a subtle before/after or internal/external representation.

You may also consider overlaying or fading one into the other if done tastefully.

The mood should hint at internal conflict, self-reckoning, and healing—but without looking too “self-help cliché.” Think masculine, introspective, modern, and editorial. Avoid overly bright or busy visuals. A minimal or clean design with strong type hierarchy is preferred.

Key Themes to Represent Visually (even abstractly):

Narcissism as a survival mechanism

The emotional cost of performance

The tension between image and authenticity

The healing journey from ego to empathy

Design References:

Run FAR Now! (uploaded) — continuity of brand and typography encouraged

Memoir-style covers like Lanterns Along the Winter Harbour, Saltwater, or A Kettle Hums at Dusk for layout feel

If using color, muted tones with contrast (black/white, sepia, desaturated blues or greys) work well

Title: A Quiet Cartographer
Subtitle (optional placement): Not every narcissist is a monster. Some are just wounded men trying their best to survive
Author: Marlon Weskett

Deliverables:

Full front cover for print sale size as previous cover, including space for subtitle and author name

Spine and back cover (leave placeholder text if no blurb is given)

Ebook cover version

High-resolution files suitable for Quillmark QPS and print use

Additional Notes:
Please ensure the tone stays emotionally resonant, masculine, and sophisticated. No stock image models or cliché therapist symbols. Use my uploaded photos only.

Looking forward to seeing your vision come to life.

Back Cover Blurb – A Quiet Cartographer
A brutally honest recovery story—about what happens after you get clean, and the ego you still have to face.
Most people think addiction ends when you put down the drink, the drug, or the chaos.
But for Marlon Weskett, sobriety was just the start.
Behind the personal development posts, six-pack selfies, and billion-rand property deals, he was still chasing the one thing rehab never took from him: the need to be admired.
This book is not a confession. It’s a dismantling.
In A Quiet Cartographer, Marlon exposes the hidden patterns of ego, control, and validation-seeking that nearly cost him everything—even after he got “better.” With fearless self-inquiry and raw storytelling, he invites readers into his recovery from performance, perfectionism, and power addiction.
Whether you’ve been the narcissist—or you’ve loved one—this book is a mirror. And what you’ll find is not just insight, but a new path forward: one where truth is more powerful than charm, and safety matters more than being impressive.
This isn’t about being perfect.
It’s about being honest.
And finally becoming someone worth trusting—especially by yourself.

Target Market(s)

Any reader wanting to read about narcissism and love

Font styles to use
Sans Serif

Colors
EB3D1F
EC4F4E
F09395
F8D3D4
FCEDEE

Requirements
Must have
• Must be better than the mock design I uploaded.

```html
<!DOCTYPE html>
<html lang="en">
<head>
<meta charset="utf-8">
<title>A Quiet Cartographer — Cover Spread</title>
<link href="https://fonts.googleapis.com/css2?family=Barlow+Condensed:ital,wght@0,300;0,400;0,500;0,600;0,700;1,700&family=Barlow:ital,wght@0,400;1,600;1,700&display=swap" rel="stylesheet">
<style>
  :root {
    --stage: #4e4e4e;
    --cover-red: #e30713;
    --spine-red: #dc0612;
    --panel-dark: #2a0607;
    --panel-deep: #1c0304;
    --ink-white: #ffffff;
    --ink-dark: #1b0808;
    --ink-maroon: #3a0708;
    --accent-red: #ff1a22;
  }
  * { box-sizing: border-box; margin: 0; padding: 0; }
  html, body { width: 1000px; height: 1200px; overflow: hidden; background: var(--stage); }
  .canvas { position: relative; width: 1000px; height: 1200px; background: var(--stage); }

  .cover {
    position: absolute; left: 40px; top: 283px; width: 920px; height: 634px;
    background: var(--cover-red); overflow: hidden;
    box-shadow: 0 4px 14px rgba(0,0,0,.35);
    font-family: "Barlow Condensed", "Arial Narrow", sans-serif;
  }

  /* Back cover */
  .back { position: absolute; left: 0; top: 0; width: 446px; height: 100%; text-align: center; color: var(--ink-white); }
  .back-hook { position: absolute; left: 20px; width: 406px; top: 66px; font-weight: 600; font-size: 16px; line-height: 20px; }
  .back-body { position: absolute; left: 10px; width: 426px; top: 128px; font-weight: 400; font-size: 13.6px; line-height: 19.8px; }
  .back-body span { display: block; white-space: nowrap; }
  .back-closing { position: absolute; left: 10px; width: 426px; top: 420px; font-family: "Barlow", Arial, sans-serif; font-style: italic; font-weight: 600; font-size: 14.5px; line-height: 20px; color: var(--ink-maroon); }

  /* Spine */
  .spine { position: absolute; left: 446px; top: 0; width: 38px; height: 100%; background: var(--spine-red); border-left: 1px solid rgba(0,0,0,.08); border-right: 1px solid rgba(0,0,0,.08); }
  .spine-title, .spine-author { position: absolute; left: 7px; writing-mode: vertical-rl; color: var(--ink-white); font-size: 21px; line-height: 24px; white-space: nowrap; }
  .spine-title { top: 124px; font-weight: 700; }
  .spine-author { top: 368px; font-weight: 300; }

  /* Front cover */
  .front { position: absolute; left: 484px; top: 0; width: 436px; height: 100%; }
  .portrait { position: absolute; left: 191px; top: 0; width: 245px; height: 100%; display: flex; }
  .portrait-raw { width: 126px; height: 100%; background: linear-gradient(180deg, var(--panel-dark) 0%, #3a0e0c 30%, #6a3a2e 62%, #4a2a22 100%); }
  .portrait-light { width: 119px; height: 100%; background: linear-gradient(180deg, var(--panel-deep) 0%, #3a1a14 28%, #9a7866 58%, #b9a69a 100%); }

  .endorsement { position: absolute; left: 46px; top: 34px; width: 340px; font-family: "Barlow", Arial, sans-serif; font-size: 10.4px; line-height: 16px; color: var(--ink-white); }
  .endorsement-name { font-family: "Barlow Condensed", sans-serif; font-weight: 700; font-size: 12.5px; color: var(--accent-red); }

  .title { position: absolute; left: 25px; top: 100px; color: var(--ink-white); text-transform: uppercase; line-height: 1; white-space: nowrap; }
  .title-lead { display: block; font-weight: 500; font-size: 42px; line-height: 44px; }
  .title-main { display: block; font-weight: 700; font-size: 80px; line-height: 72px; letter-spacing: -1px; }
  .title-main.long { font-size: 60px; line-height: 62px; }

  .subtitle { position: absolute; left: 25px; top: 346px; color: var(--ink-dark); white-space: nowrap; }
  .subtitle-soft { display: block; font-weight: 300; font-size: 21px; line-height: 22px; }
  .subtitle-strong { display: block; font-weight: 700; font-size: 44px; line-height: 42px; text-transform: uppercase; }
  .subtitle-strong.tight { font-size: 36px; line-height: 38px; }

  .author { position: absolute; left: 201px; top: 323px; writing-mode: vertical-rl; color: var(--ink-white); font-weight: 600; font-size: 40px; line-height: 44px; text-transform: uppercase; white-space: nowrap; }
</style>
</head>
<body>
<div class="canvas">
  <section class="cover">

    <div class="back">
      <p class="back-hook">Most people think addiction ends when you put down<br>the drink, the drug, or the chaos.</p>
      <p class="back-body">
        <span>But for Marlon Weskett, sobriety was just the start.</span>
        <span>Behind the personal development posts, six-pack selfies, and</span>
        <span>billion-rand property deals, he was still chasing the one thing</span>
        <span>rehab never took from him: the need to be admired.</span>
        <span>This book is not a confession. It’s a dismantling.</span>
        <span>In A Quiet Cartographer, Marlon exposes the hidden patterns of</span>
        <span>ego, control, and validation-seeking that nearly cost him</span>
        <span>everything—even after he got “better.” With fearless self-inquiry</span>
        <span>and raw storytelling, he invites readers into his recovery from</span>
        <span>performance, perfectionism, and power addiction.</span>
        <span>Whether you’ve been the narcissist—or you’ve loved one—this</span>
        <span>book is a mirror. And what you’ll find is not just insight, but a new</span>
        <span>path forward: one where truth is more powerful than charm, and</span>
        <span>safety matters more than being impressive.</span>
      </p>
      <p class="back-closing">This isn’t about being perfect.<br>It’s about being honest.<br>And finally becoming someone worth<br>trusting—especially by yourself.</p>
    </div>

    <div class="spine">
      <span class="spine-title">A QUIET CARTOGRAPHER</span>
      <span class="spine-author">MARLON WESKETT</span>
    </div>

    <div class="front">
      <div class="portrait" role="img" aria-label="Author portrait split down the middle: a raw, bearded half on the left and a clean, smiling half on the right">
        <div class="portrait-raw"></div>
        <div class="portrait-light"></div>
      </div>

      <p class="endorsement">“Whatever we’ve been through, Marlon not only makes us feel we can get over it, he gives us the tools to do exactly that.” <span class="endorsement-name">– RAVI DELACOURT</span></p>

      <h1 class="title">
        <span class="title-lead">A</span>
        <span class="title-main">Quiet</span>
        <span class="title-main long">Cartographer</span>
      </h1>

      <p class="subtitle">
        <span class="subtitle-soft">Unmasking the need</span>
        <span class="subtitle-soft">For</span>
        <span class="subtitle-strong">Control</span>
        <span class="subtitle-strong tight">Validation</span>
        <span class="subtitle-soft">And</span>
        <span class="subtitle-strong tight">Being Liked</span>
      </p>

      <p class="author">Marlon Weskett</p>
    </div>

  </section>
</div>
</body>
</html>
```